Harborline Stay Collective Business Card Design

Design a business card for Harborline Stay Collective. Look at the website for colors and reference. Card should have logo, name, title, office number, mobile number, email, URL and a tagline like, "Luxury Hotel & Resort Email Marketing" (This might change).

https://www.harborlinestaycollective.net

The rest I will leave up to your imagination.

Contact Information for Business Card

Logo, name, title, office number, mobile number, email, URL and a tagline like, "Luxury Hotel & Resort Email Marketing" (This might change).

```html
<!DOCTYPE html>
<html lang="en">
<head>
<meta charset="utf-8">
<title>Harborline Stay Collective – Business Card</title>
<link href="https://fonts.googleapis.com/css2?family=Jost:wght@300;400;500;600&family=Great+Vibes&display=swap" rel="stylesheet">
<style>
  :root{
    --backdrop:#4f4f4f;
    --navy:#003566;
    --teal:#4ac4cb;
    --paper:#e6e6e6;
    --wave-line:#333333;
    --orange:#f7830f;
    --ink:#333333;
    --white:#ffffff;
  }
  *{margin:0;padding:0;box-sizing:border-box}
  html,body{width:960px;height:1200px;overflow:hidden}
  body{background:var(--backdrop);font-family:'Jost',sans-serif;position:relative}

  .card{position:absolute;left:60px;width:840px;height:480px;border-radius:44px;overflow:hidden;
        background:var(--paper);box-shadow:6px 8px 14px rgba(0,0,0,.45)}
  .card--front{top:83px}
  .card--back{top:638px}

  .card__art{position:absolute;inset:0}

  .brand{position:absolute;left:0;right:0;top:222px;text-align:center;color:var(--white);
         font-weight:600;text-transform:uppercase}
  .brand__main{display:block;font-size:56px;line-height:58px;letter-spacing:2px}
  .brand__sub{display:block;font-size:18px;line-height:20px;letter-spacing:6px;margin-top:2px}

  .tagline{position:absolute;left:0;right:0;top:308px;text-align:center;color:var(--white);
           font-family:'Great Vibes',cursive;font-size:35px;line-height:46px}

  .brand-small{position:absolute;right:44px;top:38px;text-align:center;color:#111111;
               font-weight:600;text-transform:uppercase}
  .brand-small__main{display:block;font-size:24px;line-height:26px;letter-spacing:1px}
  .brand-small__sub{display:block;font-size:8.5px;line-height:10px;letter-spacing:2.4px;margin-top:2px}

  .person{position:absolute;left:112px;top:222px}
  .person__name{font-size:33px;font-weight:400;color:var(--navy);line-height:1;letter-spacing:.5px}
  .person__name strong{font-weight:500}
  .person__role{font-size:22px;font-weight:300;color:var(--orange);margin-top:6px;line-height:1.2}

  .divider{position:absolute;left:356px;top:179px;width:3px;height:117px;background:var(--teal)}

  .icons{position:absolute;left:374px;top:180px;display:flex;gap:12px}
  .icon{width:29px;height:29px}

  .contacts{position:absolute;left:374px;top:216px;list-style:none;color:var(--ink);
            font-size:25px;font-weight:400;line-height:26px;letter-spacing:.5px}

  .url-band{position:absolute;left:0;right:0;bottom:0;height:47px;background:var(--navy);
            color:var(--white);text-align:center;font-size:23px;line-height:47px;letter-spacing:3.5px}
</style>
</head>
<body>

<section class="card card--front">
  <svg class="card__art" viewBox="0 0 840 480" aria-hidden="true">
    <defs>
      <filter id="arc-shadow" x="-10%" y="-20%" width="120%" height="160%">
        <feDropShadow dx="0" dy="6" stdDeviation="7" flood-color="#000" flood-opacity=".25"/>
      </filter>
    </defs>
    <path d="M0 0H840V429L502 431C466 431 466 417 430 417C394 417 394 433 358 433C322 433 322 417 286 417C250 417 250 433 214 433C178 433 178 417 142 417C106 417 106 433 70 433C45 433 25 418 0 418Z" fill="var(--teal)"/>
    <path d="M0 418C25 418 45 433 70 433C106 433 106 417 142 417C178 417 178 433 214 433C250 433 250 417 286 417C322 417 322 433 358 433C394 433 394 417 430 417C466 417 466 431 502 431L840 429" fill="none" stroke="var(--wave-line)" stroke-width="4"/>
    <path d="M0 0H840V20Q425 300 16 20H0Z" fill="var(--navy)" filter="url(#arc-shadow)"/>
    <g fill="none" stroke="var(--white)" stroke-width="2.6" stroke-linejoin="round">
      <path d="M381 105l4.5 9.6 10.4 1.3-7.6 7.2 2 10.4-9.3-5.1-9.3 5.1 2-10.4-7.6-7.2 10.4-1.3z"/>
      <path d="M420 82l5.6 11.9 13 1.6-9.5 9 2.4 12.9-11.5-6.3-11.5 6.3 2.4-12.9-9.5-9 13-1.6z"/>
      <path d="M459 105l4.5 9.6 10.4 1.3-7.6 7.2 2 10.4-9.3-5.1-9.3 5.1 2-10.4-7.6-7.2 10.4-1.3z"/>
    </g>
  </svg>
  <h1 class="brand"><span class="brand__main">Harborline</span><span class="brand__sub">Stay Collective</span></h1>
  <p class="tagline">Luxury Hotel &amp; Resort Email Marketing</p>
</section>

<section class="card card--back">
  <div class="brand-small"><span class="brand-small__main">Harborline</span><span class="brand-small__sub">Stay Collective</span></div>

  <div class="person">
    <h2 class="person__name"><strong>Marisol</strong> Trevane</h2>
    <p class="person__role">Job Title</p>
  </div>

  <div class="divider"></div>

  <div class="icons" aria-hidden="true">
    <svg class="icon" viewBox="0 0 28 28"><circle cx="14" cy="14" r="14" fill="var(--navy)"/><path d="M9.5 8.5c1-.6 1.6-.3 2.2.8l.8 1.6c.3.7.1 1.2-.5 1.6l-.6.4c.6 1.6 1.6 2.7 3.2 3.4l.5-.6c.4-.6.9-.8 1.6-.5l1.6.8c1 .6 1.3 1.2.7 2.2-.8 1.3-2 1.6-3.4 1.1-3-1.1-5.1-3.3-6.3-6.3-.5-1.4-.4-2.7.2-3.5z" fill="var(--white)"/><path d="M16 8.5a4 4 0 0 1 3.5 3.5M16 10.6a2 2 0 0 1 1.4 1.4" fill="none" stroke="var(--white)" stroke-width="1.1" stroke-linecap="round"/></svg>
    <svg class="icon" viewBox="0 0 28 28"><circle cx="14" cy="14" r="14" fill="var(--navy)"/><path d="M7 11.5c0-2 3.2-3 7-3s7 1 7 3v1.2h-3.2v-1.6h-7.6v1.6H7z" fill="var(--white)"/><path d="M10.5 13.3h7l2 5.2H8.5z" fill="var(--white)"/><circle cx="14" cy="15.8" r="1.4" fill="var(--navy)"/></svg>
    <svg class="icon" viewBox="0 0 28 28"><circle cx="14" cy="14" r="14" fill="var(--navy)"/><rect x="7.5" y="9" width="12" height="8.5" rx="1" fill="var(--white)"/><path d="M7.8 9.5l5.7 4.3 5.7-4.3" fill="none" stroke="var(--navy)" stroke-width="1.1"/><circle cx="19.5" cy="18" r="3" fill="var(--white)" stroke="var(--navy)" stroke-width="1"/><circle cx="19.5" cy="18" r="1" fill="none" stroke="var(--navy)" stroke-width=".9"/></svg>
  </div>

  <ul class="contacts">
    <li>808.555.0147</li>
    <li>+34 600 555 214</li>
    <li>info@harborlinestaycollective.net</li>
  </ul>

  <p class="url-band">www.harborlinestaycollective.net</p>
</section>

</body>
</html>
```